The CoinHarbor Flyer (not postcard)

The CoinHarbor is my financial planning practice. I offer planning and wealth management services to clients.

I want a full 8.5x11 double sided flyer outlining my services - something I can hand out to propsects in person. It is a simple word document that you can see under my account called The CoinHarbor Flyer. I just need it to look very professional and colorful. My logo colors are nice and you can see other things I have made to give you an idea. The only reason I labeled this project is a postcard is that was the only option through Printomix (how I found you).

I like the phone - fee free to call my cell at 682 317 4096. the winner will be someone who works with me so its as great as it can be.
Updates

Just to be clear I want a full 8.5x11 double sided flyer - any problems email me at marcus@coinharborgroup.net

thx 

Hi everyone,

No more designs are needed. I have what I need. Thanks 

Target Market(s)

prospects - people with wealth

Industry/Entity Type

Financial

Font styles to use
Serif

Colors
3276b5
f68e4e

Requirements
Must have
• I am going for simplicity with the flyer. If you want less words, I can edit the word doc down further. The text needs to be neatly organized so it is easy to follow. Please match my logo colors.

Nice to have
• financial services - i have 3 sections there. that should all be aligned horizontally next to one another so as to take up less space.

wealth management is its own little world so i would like the company info, financial planning, and wealth management grouped in 3 different sections.

```html
<!DOCTYPE html>
<html lang="en">
<head>
<meta charset="utf-8">
<title>The CoinHarbor Flyer</title>
<link rel="stylesheet" href="https://fonts.googleapis.com/css2?family=Tinos:ital,wght@0,400;0,700;1,400&display=swap">
<style>
:root{
  --navy:#1a5687;
  --navy-deep:#0f3f6a;
  --orange:#e8892a;
  --grey:#dcdcdd;
  --ink:#2a2a2a;
  --muted:#8a8a8a;
  --backdrop:#e9e7e3;
  --white:#ffffff;
}
*{margin:0;padding:0;box-sizing:border-box}
html,body{width:1200px;height:900px;overflow:hidden}
body{background:var(--backdrop);font-family:"Tinos","Times New Roman",serif;color:var(--ink);position:relative}
.page{position:absolute;background:var(--white);box-shadow:0 3px 10px rgba(0,0,0,.25)}
.front{left:35px;top:140px;width:545px;height:705px}
.back{left:628px;top:47px;width:547px;height:705px}

/* front */
.hero{position:absolute;left:0;top:0;width:545px;height:225px;background:linear-gradient(180deg,#1d5b8e 0%,#2f78b0 45%,#174d7c 100%)}
.hero-title{position:absolute;left:16px;top:86px;font-style:italic;font-size:27px;color:var(--white);letter-spacing:.3px}
.about{position:absolute;left:0;top:225px;width:545px;height:143px;background:var(--navy);border-top:1px solid var(--orange);padding:14px 16px 0;color:var(--white)}
.section-title{color:var(--orange);font-size:19px;margin-bottom:10px}
.about p{font-size:9.5px;line-height:1.25;margin-bottom:7px}
.why{position:absolute;left:0;top:368px;width:545px;height:189px;background:var(--grey);border-bottom:1px solid var(--orange)}
.portrait{position:absolute;left:0;top:8px;width:135px;height:181px;background:linear-gradient(180deg,#e4e4e4 0%,#c9c9c9 55%,#3a3a3e 100%)}
.why-body{position:absolute;left:148px;top:12px;width:385px}
.why-body h3{font-weight:400;font-size:15px;color:var(--navy);margin-bottom:2px}
.bullets{list-style:none;font-size:9.5px;line-height:1.35;margin-bottom:10px}
.bullets li::before{content:"▪ ";color:var(--orange)}
.options{list-style:none;font-size:9.5px;line-height:1.35}
.options li{padding-left:10px;text-indent:-10px}
.footer-front{position:absolute;left:0;top:557px;width:545px;height:133px}
.brand{position:absolute;left:16px;top:40px;display:flex;align-items:center;gap:8px}
.brand-mark{width:22px;height:22px;border-radius:50%;background:var(--navy)}
.brand-name{font-size:27px;color:var(--navy)}
.tagline{position:absolute;left:46px;top:76px;font-size:9px;color:var(--orange)}
.contact{position:absolute;left:374px;top:38px;font-size:9.5px;line-height:1.35;color:var(--muted)}
.contact b{font-weight:400;color:var(--orange)}
.orange-bar{position:absolute;left:0;bottom:0;width:100%;height:15px;background:var(--orange)}

/* back */
.services{position:absolute;left:0;top:0;width:547px;height:146px;background:var(--navy);color:var(--white);padding:14px 18px 0}
.services h2{font-weight:400;font-size:19px;line-height:1}
.services h2 sup{font-size:10px}
.services .lead{font-weight:700;font-size:9.5px;margin:3px 0 7px}
.columns{display:flex}
.col{font-size:9.5px;line-height:1.35}
.col:nth-child(1){width:182px}
.col:nth-child(2){width:174px}
.col h4{color:var(--orange);font-size:10px}
.wealth{position:absolute;left:0;top:146px;width:547px;padding:10px 18px 0}
.wealth h2{font-weight:400;font-size:19px;color:var(--navy);line-height:1}
.wealth h3{font-size:11px;margin:7px 0 1px}
.principles{list-style:none;font-size:9.5px;line-height:1.35}
.principles li::before{content:"▪ ";color:var(--orange)}
.rule{border:0;border-top:1px solid #555;margin:7px 0 8px}
.wealth h4.subhead{font-size:11px;color:var(--navy);margin-bottom:5px}
.method{font-size:7.8px;line-height:1.32;margin-bottom:5px}
.method .label{color:var(--orange);font-weight:700;font-size:8px}
.disclaimer{position:absolute;left:0;top:578px;width:547px;height:113px;background:var(--navy);color:var(--white);padding:9px 18px 0;font-size:7.6px;line-height:1.3}
.disclaimer p{margin-bottom:6px}
.disclaimer p.tight{margin-bottom:0}
</style>
</head>
<body>

<section class="page front">
  <div class="hero" role="img" aria-label="Blue ocean wave breaking behind a sailboat"></div>
  <h1 class="hero-title">Investment Innovation.</h1>

  <div class="about">
    <h2 class="section-title">About Us</h2>
    <p>The CoinHarbor is the practice of <b>Marcus Delaney, CHFC, CLU.</b></p>
    <p>The CoinHarbor provides comprehensive financial advice and asset management for over 200 clients.</p>
    <p>We have the privilege of managing over $22 million for those households.</p>
    <p>Marcus is a 10 year financial planning veteran who graduated from Halvern University in Kent, OH with a double major in finance and accounting. After becoming fully licensed, he started building his practice.</p>
  </div>

  <div class="why">
    <div class="portrait" role="img" aria-label="Portrait of the advisor in a dark suit"></div>
    <div class="why-body">
      <h3>Why Plan with us</h3>
      <ul class="bullets">
        <li>Marcus's age</li>
        <li>Strong educational focus for clients</li>
        <li>Protect and grow wealth through insurance and investments</li>
        <li>Reduce your tax liability</li>
        <li>Efficiently leave assets to heirs</li>
      </ul>
      <h3>Client Service Options</h3>
      <ol class="options">
        <li>1) Asset Management: We charge a flat 1% fee on assets under management.</li>
        <li>2) Financial Planning &amp; Advice : Flat yearly fee for comprehensive financial and protection planning advice.</li>
        <li>3) CPortfolio Asset Management:&nbsp; Flat fee to use our portfolio models.</li>
      </ol>
    </div>
  </div>

  <div class="footer-front">
    <div class="brand"><span class="brand-mark"></span><span class="brand-name">The CoinHarbor</span></div>
    <div class="tagline">Financial Services &amp; Wealth Management</div>
    <address class="contact" style="font-style:normal">
      212 Larkmoor Ave. Suite 310<br>
      Bellhaven, NY 11902<br>
      <b>Phone:</b> 682-317-4096<br>
      <b>Fax</b>&nbsp;&nbsp;&nbsp;: 682-317-5520<br>
      <b>Email</b> : marcus@coinharborgroup.net<br>
      <b>Web</b>&nbsp;&nbsp;&nbsp;: www.coinharbor.net
    </address>
  </div>
  <div class="orange-bar"></div>
</section>

<section class="page back">
  <div class="services">
    <h2>Financial Services<sup>*</sup>:</h2>
    <p class="lead">We advise clients on all of the following areas in your custom financial plan.</p>
    <div class="columns">
      <div class="col">
        <h4>Personal Finance &amp; Life Events</h4>
        Cash Management<br>Cash Flow Management<br>Retirement Planning<br>Education Planning<br>Home Purchase<br>Liability Management
      </div>
      <div class="col">
        <h4>Protection Planning</h4>
        Life Insurance<br>Disability Insurance<br>Long Term Care Insurance<br>Business Insurance<br>Supplemental Insurance
      </div>
      <div class="col">
        <h4>Tax &amp; Estate Planning</h4>
        IRAs<br>Roth IRAs<br>401(k) &amp; Roth 401(k)<br>Small Business Retirement Plans<br>Legacy Planning
      </div>
    </div>
  </div>

  <div class="wealth">
    <h2>Wealth Management</h2>
    <h3>The CoinHarbor Investment Principles</h3>
    <ul class="principles">
      <li>Creation of an investment policy statement</li>
      <li>Managing Client Emotions &amp; Behaviors: Faith in the future, patience, and discipline</li>
      <li>Global Diversification</li>
      <li>Avoiding Large Losses</li>
      <li>Being Steady &amp; Consistent</li>
      <li>Protect in bad times while participating in good times.</li>
      <li>Liquidity</li>
    </ul>
    <hr class="rule">
    <h4 class="subhead">Asset Allocation Methodologies</h4>
    <p class="method"><span class="label">Asset Allocation Methodologies</span><br>Offense:&nbsp; Buy &amp; Hold<br>This approach is designed to closely track the broader investment markets by using a target mix of equities, fixed income, and cash. Returns will be impacted by market exposure.</p>
    <p class="method"><span class="label">Offense Models:</span><br>Passive Cap ETF: 11 Submodels<br>Passive Fundamental ETF:&nbsp; 11 Submodels<br>Diversified Income: 4 Submodels<br>Global Frontier: 3 Submodels</p>
    <p class="method"><span class="label">Defense:&nbsp; Active Management</span><br>This approach is designed to take protect clients in bad times by hiring skilled money managers.&nbsp; These money managers can use many different strategies to achieve their goals including tactical, absolute return, and alternative investment approaches.</p>
    <p class="method"><span class="label">Defense Models:&nbsp; The Steady Guard</span><br>Aggressive<br>Moderate Aggressive<br>Moderate<br>Moderate Conservative<br>Conservative</p>
    <p class="method"><span class="label">Preservation Municipal Bond</span><br>Insurance Based<br>Cash Value Life Insurance<br>Annuities: Fixed, Immediate, &amp; Variable with Income Guarantee</p>
  </div>

  <div class="disclaimer">
    <p class="tight">*Investments involve both risk and the possible loss of principal. There is no insurance that these principles will avoid losses.</p>
    <p>**Please consult with a tax advisor as they are an integral part of our team.</p>
    <p>Registered Representative offering securities through Meridian Crest Financial Services, Inc., Member NFRB, SIPX.*These services are offered through our broker-dealer: Meridian Crest Financial Services, Inc. &amp; Meridian Crest Advisors, An SEC Registered Investment Advisor.&nbsp; Investment Advisory services offered through Meridian Crest Advisors, Inc., an SEC Registered Investment Advisor.</p>
    <p>The CoinHarbor is independent of Meridian Crest Financial Services, Inc. &amp; Meridian Crest Advisors Inc. The CoinHarbor email is hosted by Meridian Crest Financial Services, Inc.Investments involve both risk and the possible loss of principal. There is no insurance that these principles will avoid losses.</p>
  </div>
  <div class="orange-bar"></div>
</section>

</body>
</html>
```